Linkmesa and Glimtoria advertising

We need Linkmesa and Glimtoria ads. Simple ad with Alaska themed background.
This ad is to introduce our new ZENIRO Internet service.
--Speeds to 500 mpbs
-- Packages start at only $89.99 for speeds to 100mbps
-- Fiber Optic based connection, Not satellite
-- Extreme low latency, consistent speeds
--FREE equipment, FREE Installation, FREE wifi router, First month of service FREE

```html
<!DOCTYPE html>
<html lang="en">
<head>
<meta charset="UTF-8">
<title>ZENIRO Internet service – Nordvale Satellite</title>
<link rel="stylesheet" href="https://fonts.googleapis.com/css2?family=Montserrat:wght@300;400;500;600;700&display=swap">
<style>
  :root {
    --navy-deep: #03052e;
    --navy: #0a0f73;
    --sky-top: #0e3a66;
    --sky-mid: #0a2456;
    --snow: #5aa6e0;
    --snow-light: #a9dcf7;
    --cyan: #12e2f2;
    --white: #ffffff;
    --wifi: #4a86e4;
    --logo-ink: #111111;
  }
  * { margin: 0; padding: 0; box-sizing: border-box; }
  html, body { width: 1200px; height: 1200px; overflow: hidden; background: var(--navy-deep); }
  .ad {
    position: relative;
    width: 1200px;
    height: 1200px;
    overflow: hidden;
    font-family: "Montserrat", sans-serif;
    color: var(--white);
    background: linear-gradient(180deg, var(--sky-top) 0%, var(--sky-mid) 35%, var(--navy-deep) 62%, var(--navy) 85%, var(--navy) 100%);
  }
  .sky-scene {
    position: absolute;
    left: 0; top: 0;
    width: 1200px; height: 560px;
    background: linear-gradient(160deg, rgba(30,140,190,0.35) 0%, rgba(14,58,102,0.15) 55%, rgba(3,5,46,0) 100%);
  }
  .landscape-scene {
    position: absolute;
    left: 0; bottom: 0;
    width: 1200px; height: 206px;
    background: linear-gradient(180deg, rgba(90,166,224,0) 0%, var(--snow) 55%, var(--snow-light) 100%);
  }
  .brand-mark {
    position: absolute;
    left: 860px; top: 142px;
    width: 263px; height: 69px;
    background: var(--white);
    display: flex; align-items: center; justify-content: center;
  }
  .brand-mark .name { font-weight: 600; font-size: 25px; color: var(--logo-ink); }
  .intro {
    position: absolute; left: 87px; top: 241px;
    font-size: 54px; font-weight: 300; line-height: 1; letter-spacing: -0.5px;
    white-space: nowrap;
  }
  .product-name { font-weight: 700; line-height: 1; }
  .product-name span { position: absolute; white-space: nowrap; }
  .product-name .initial { left: 84px; top: 279px; font-size: 274px; }
  .product-name .rest { left: 262px; top: 402px; font-size: 131px; letter-spacing: 1px; }
  .tagline {
    position: absolute; left: 93px; top: 548px;
    font-size: 52px; font-weight: 500; line-height: 1; color: var(--cyan);
    white-space: nowrap;
  }
  .features {
    position: absolute; left: 78px; top: 676px;
    list-style: none;
    font-size: 29px; font-weight: 500; line-height: 43.8px;
    white-space: nowrap;
  }
  .features li { position: relative; padding-left: 34px; }
  .features li::before {
    content: ""; position: absolute; left: 1px; top: 14px;
    width: 14px; height: 14px; border-radius: 50%; background: var(--cyan);
  }
  .wifi-icon { position: absolute; left: 800px; top: 810px; }
</style>
</head>
<body>
<main class="ad">
  <div class="sky-scene" role="img" aria-label="Alaskan night sky with a glowing aurora streak and a bright star"></div>
  <div class="landscape-scene" role="img" aria-label="Snow-covered Alaskan mountains under blue night light"></div>

  <div class="brand-mark">
    <span class="name">Nordvale Satellite</span>
  </div>

  <p class="intro">Introduce our new</p>
  <h1 class="product-name"><span class="initial">Z</span><span class="rest">ENIRO</span></h1>
  <h2 class="tagline">Internet service</h2>

  <ul class="features">
    <li>Speeds to 500 mpbs</li>
    <li>Packages start at only $89.99 for speeds to 100mbps</li>
    <li>Fiber Optic based connection, Not satellite</li>
    <li>Extreme low latency, consistent speeds</li>
    <li>FREE equipment, FREE Installation,<br>FREE wifi router, First month of service FREE</li>
  </ul>

  <svg class="wifi-icon" width="400" height="350" viewBox="0 0 400 350" aria-hidden="true">
    <g fill="none" stroke="var(--wifi)" stroke-linecap="round">
      <path d="M20 125 Q212 -30 400 125" stroke-width="40"/>
      <path d="M75 185 Q212 70 350 185" stroke-width="38"/>
      <path d="M130 240 Q212 170 294 240" stroke-width="36"/>
    </g>
    <circle cx="215" cy="289" r="56" fill="var(--wifi)"/>
  </svg>
</main>
</body>
</html>
```